2nd Generation Blind Manufacturer & Retailer Needs A Stationary Set

We need a stationary set for a family business located the in the Whitsundays (QLD). We retail and manufacture blinds awnings and shutters. Second generation, in operation for over 30 years.

Final draft must include at minimum:

Business Card (2 Sided)
Letterhead
Presentation Folder

Target Market(s)

home owners, landlords, builders, real estate agents, shopping centres

Industry/Entity Type

Textile

Requirements
Must have
• Design needs to work in mono as well as colour print
Nice to have
• Relevant to the textile industry
Should not have
• The inclusion of blinds, awnings or shutters is an automatic no-no

```html
<!DOCTYPE html>
<html lang="en">
<head>
<meta charset="utf-8">
<title>Harlow Blinds – Business Card</title>
<link rel="stylesheet" href="https://fonts.googleapis.com/css2?family=Source+Sans+3:wght@400;600&display=swap">
<style>
  :root {
    --page: #e6e3df;
    --card: #121212;
    --card-edge: #1d1d1d;
    --brand-grey: #8c8c8c;
    --rule-grey: #6a6a6a;
    --text-light: #e4e4e4;
    --title-purple: #8a2c9c;
    --icon-grey: #b9b9b9;
  }
  * { box-sizing: border-box; margin: 0; padding: 0; }
  html, body { width: 1200px; height: 814px; overflow: hidden; }
  body {
    background: var(--page);
    font-family: "Source Sans 3", "Myriad Pro", Arial, sans-serif;
    position: relative;
  }
  .card {
    position: absolute;
    width: 525px;
    height: 300px;
    background: var(--card);
    border: 1px solid var(--card-edge);
    box-shadow: 0 10px 28px rgba(0,0,0,.25);
  }
  .card--back { left: 45px; top: 257px; }
  .card--front { left: 630px; top: 257px; }

  .brand {
    position: absolute;
    display: flex;
    align-items: center;
  }
  .brand__mark {
    width: 46px; height: 46px;
    background: var(--brand-grey);
  }
  .brand__rule {
    width: 1px; height: 70px;
    background: var(--rule-grey);
    margin: 0 12px 0 14px;
  }
  .brand__name {
    color: var(--brand-grey);
    font-weight: 600;
    font-size: 27px;
    line-height: 27px;
    letter-spacing: .5px;
    text-transform: uppercase;
  }
  .card--back .brand { left: 42px; top: 118px; }
  .card--back .brand__mark { width: 40px; height: 40px; }
  .card--back .brand__rule { height: 58px; }
  .card--back .brand__name { font-size: 22px; line-height: 23px; }

  .card--front .brand { left: 118px; top: 84px; }
  .card--front .brand__name { font-size: 32px; line-height: 32px; }

  .web-address {
    position: absolute;
    left: 0; right: 0; top: 212px;
    text-align: center;
    color: var(--text-light);
    font-size: 12px;
    letter-spacing: 6px;
  }

  .contact {
    position: absolute;
    left: 272px; top: 62px;
    color: var(--text-light);
    font-size: 13.5px;
    line-height: 18px;
  }
  .contact__name {
    color: var(--brand-grey);
    font-weight: 600;
    font-size: 16px;
    letter-spacing: .5px;
    text-transform: uppercase;
  }
  .contact__title { color: var(--title-purple); margin-bottom: 4px; }
  .contact__row { display: flex; align-items: center; gap: 8px; }
  .contact__row svg { width: 12px; height: 12px; flex: none; fill: var(--icon-grey); }
</style>
</head>
<body>

  <section class="card card--back" aria-label="Business card back">
    <div class="brand">
      <div class="brand__mark"></div>
      <div class="brand__rule"></div>
      <div class="brand__name">Harlow<br>Blinds</div>
    </div>
    <div class="contact">
      <p class="contact__name">Dana Reyes</p>
      <p class="contact__title">CEO/Founder</p>
      <p>214 Coral Bay Road</p>
      <p>Airlie Beach, QLD 4802</p>
      <p class="contact__row">
        <svg viewBox="0 0 12 12" aria-hidden="true"><path d="M2.4 0.8l2 2.2-1 1.3c.7 1.5 1.8 2.6 3.3 3.3l1.3-1 2.2 2-1.2 2.2C5.5 10.6 1.4 6.5 1.2 2z"/></svg>
        074 946 1280
      </p>
      <p class="contact__row">
        <svg viewBox="0 0 12 12" aria-hidden="true"><path d="M3 0h6v12H3zM4 1.5v8h4v-8z"/></svg>
        0412 557 903
      </p>
      <p class="contact__row">
        <svg viewBox="0 0 12 12" aria-hidden="true"><path d="M0 2h12v8H0zM1 3v.4l5 3.2 5-3.2V3z"/></svg>
        hello@harlowblinds.com
      </p>
      <p class="contact__row">
        <svg viewBox="0 0 12 12" aria-hidden="true"><circle cx="6" cy="6" r="5.5"/><path d="M6 .5v11M.5 6h11M3 1.6c2 2.6 2 6.2 0 8.8M9 1.6c-2 2.6-2 6.2 0 8.8" stroke="#121212" stroke-width=".8" fill="none"/></svg>
        www.harlowblinds.com
      </p>
    </div>
  </section>

  <section class="card card--front" aria-label="Business card front">
    <div class="brand">
      <div class="brand__mark"></div>
      <div class="brand__rule"></div>
      <div class="brand__name">Harlow<br>Blinds</div>
    </div>
    <p class="web-address">www.harlowblinds.com</p>
  </section>

</body>
</html>
```